POS Systems

Redesign existing site with improvement in layout an sitemap

I need Responsive PSD Designs

Current site is http://brindlepay.com.au/

Client is no longer selling Cash Registers

Only doing Touch Screen Point of Sale Systems
for 4 main industries (Restaurants and Cafes, Grocery and Convenience, Fruit & Veg, Bars, Pubs and Clubs)

Sitemap:

1. Home - With 4 types of businesses serviced, 4 Video Testimonials, End Of Financial Year Sale, Finance Options

2. Our System - Video, text, Boxes of 4 Different Industries, Book a Consultation / Call
Drop down menu for each different industry

(Restaurants and Cafes, Grocery and Convenience, Fruit & Veg, Bars, Pubs and Clubs)

3. About Us - text about history

4. Events

5. Testimonials

6. News - blog page

7. Gallery

8. Contact

#I need PSD Files and I will convert to Wordpress Myself

#I need the Each page designed please except Gallery

# I will build the site on Wordpress

# Designs will need to include responsiveness

Target Market(s)

Business Owners who want to upgrade to a POS System to increase productivity

Industry/Entity Type

Industry

Requirements
Must have
• Menu as above
Responsive Design

```html
<!DOCTYPE html>
<html lang="en">
<head>
<meta charset="utf-8">
<title>BrindlePay – Point of Sale Solutions</title>
<link href="https://fonts.googleapis.com/css2?family=Open+Sans:wght@300;400;600;700&display=swap" rel="stylesheet">
<style>
:root{
  --brand-blue:#3c4e9c;
  --brand-green:#7cbb43;
  --green-dark:#6aa635;
  --hero-bg:#f3f3f3;
  --text:#666;
  --heading:#3c4e9c;
  --dark:#333;
  --border:#dcdcdc;
}
*{box-sizing:border-box;margin:0;padding:0}
html,body{width:742px;height:1200px;overflow:hidden}
body{font-family:"Open Sans",Arial,sans-serif;background:#fff;color:var(--text);position:relative}
.site-header{position:absolute;left:0;top:0;width:742px;height:55px;background:var(--brand-blue);color:#fff}
.brand{position:absolute;left:98px;top:9px}
.brand-name{font-size:18px;font-weight:600;display:flex;align-items:center;gap:5px;line-height:22px}
.brand-name .dot{width:9px;height:9px;border-radius:50%;background:#fff}
.brand-tag{font-size:6.5px}
.phone{position:absolute;left:505px;top:8px;font-size:13px;font-weight:300;display:flex;align-items:center;gap:4px}
.main-nav{position:absolute;left:217px;top:34px;display:flex;gap:20px;font-size:9.4px;font-weight:700}
.toolbar{position:absolute;left:0;top:55px;width:742px;height:28px;background:var(--brand-green);color:#fff;font-size:9px;font-weight:700}
.categories{position:absolute;left:119px;top:8px;display:flex;align-items:center;gap:8px}
.search-label{position:absolute;left:232px;top:9px}
.search-box{position:absolute;left:311px;top:5px;width:266px;height:19px;background:var(--green-dark);border:1px solid #8cc95a}
.search-box span{position:absolute;left:7px;top:4px;font-size:7px;font-weight:400;color:#d9edc7}
.search-btn{position:absolute;right:2px;top:2px;width:44px;height:13px;background:var(--brand-blue);font-size:7.5px;text-align:center;line-height:13px}
.cart{position:absolute;left:591px;top:9px;font-size:8px;display:flex;align-items:center;gap:4px}
.hero{position:absolute;left:0;top:83px;width:742px;height:222px;background:var(--hero-bg)}
.hero-media{position:absolute;left:122px;top:30px;width:181px;height:172px;border-radius:10px;background:linear-gradient(160deg,#444,#1a1a1a)}
.hero-text{position:absolute;left:335px;top:86px;width:290px;font-size:12px;font-weight:300;line-height:17px;color:#666}
.arrow{position:absolute;width:14px;height:24px}
.section-title{position:absolute;left:0;width:742px;text-align:center;font-size:12px;font-weight:700;color:var(--heading)}
.cards{position:absolute;left:80px;display:flex;gap:11px}
.card{width:137px}
.card-label{font-size:10px;color:var(--dark);height:14px;margin-bottom:10px}
.card-img{width:137px;height:80px}
.card-title{font-size:8.2px;font-weight:700;color:#555;margin-top:9px;white-space:nowrap}
.card-meta{font-size:6.3px;color:#555;margin-top:5px;white-space:nowrap}
.quote{font-size:17px;font-weight:700;color:#555;height:14px;line-height:20px;margin-top:3px;margin-left:-6px}
.card-text{font-size:8.4px;font-weight:300;color:#555;line-height:14.8px;margin-top:6px;letter-spacing:-.1px}
.btn{display:inline-block;background:var(--brand-green);color:#fff;font-size:8.6px;font-weight:600;padding:0 10px;height:23px;line-height:23px;margin-top:9px}
.products{position:absolute;left:78px;top:922px;display:flex;gap:13px}
.product{width:187px}
.product-frame{height:100px;border:1px solid var(--border);display:flex;align-items:center;justify-content:center}
.product-frame .pic{width:92px;height:72px}
.promo{flex-direction:column;color:#fff;text-align:center;border:none}
.promo-sale{background:var(--brand-blue)}
.promo-finance{background:var(--brand-green)}
.promo-kicker{font-size:8px;font-weight:600;letter-spacing:1px;text-transform:uppercase}
.promo-title{font-size:14px;font-weight:700;line-height:18px;margin-top:4px}
.promo-note{font-size:8.5px;font-weight:300;margin-top:4px}
.product-text{font-size:8.4px;font-weight:300;color:#555;line-height:14.8px;margin-top:9px}
.site-footer{position:absolute;left:0;top:1136px;width:742px;height:64px;background:var(--brand-blue);color:#fff}
.footer-nav{display:flex;justify-content:center;gap:14px;font-size:9.6px;margin-top:19px;margin-left:-14px}
.copyright{text-align:center;font-size:9.6px;margin-top:17px}
</style>
</head>
<body>
<header class="site-header">
  <div class="brand">
    <div class="brand-name">BrindlePay <span class="dot"></span></div>
    <div class="brand-tag">BrindlePay Point of Sale Solutions</div>
  </div>
  <div class="phone">
    <svg width="9" height="11" viewBox="0 0 9 11"><path d="M2 0 L4 2.5 L3 4 C3.5 5.5 4.5 7 6 7.5 L7.5 6.5 L9 9 L7 11 C3 10 0 6 0 2 Z" fill="#fff"/></svg>
    1300 555 019
  </div>
  <nav class="main-nav">
    <span>Home</span><span>Our System</span><span>About Us</span><span>Events</span><span>Testimonials</span><span>Blog</span><span>Gallery</span><span>Contact</span>
  </nav>
</header>

<div class="toolbar">
  <div class="categories">Categories
    <svg width="8" height="5" viewBox="0 0 8 5"><path d="M1 1 L4 4 L7 1" stroke="#fff" stroke-width="1.5" fill="none"/></svg>
  </div>
  <div class="search-label">Search Products</div>
  <div class="search-box"><span>Enter The keywords</span><div class="search-btn">Search</div></div>
  <div class="cart">
    <svg width="14" height="11" viewBox="0 0 14 11"><path d="M0 1 H3 L5 8 H12 L13.5 3 H4" stroke="#fff" stroke-width="1.2" fill="none"/><circle cx="6" cy="10" r="1" fill="#fff"/><circle cx="11" cy="10" r="1" fill="#fff"/></svg>
    Add To Cart &nbsp;$0.00
  </div>
</div>

<section class="hero">
  <svg class="arrow" style="left:58px;top:105px" viewBox="0 0 14 24"><path d="M12 2 L3 12 L12 22" stroke="#bbb" stroke-width="3" fill="none"/></svg>
  <div class="hero-media" role="img" aria-label="Touch screen point of sale terminal"></div>
  <p class="hero-text">Specially designed for fruit and veg stores, BrindlePay combines fast graphical touch screens with the latest in scan and scale technology.</p>
  <svg class="arrow" style="left:669px;top:105px" viewBox="0 0 14 24"><path d="M2 2 L11 12 L2 22" stroke="#bbb" stroke-width="3" fill="none"/></svg>
</section>

<section>
  <svg class="arrow" style="left:80px;top:326px" viewBox="0 0 14 24"><path d="M12 3 L4 12 L12 21" stroke="#555" stroke-width="2.6" fill="none"/></svg>
  <h2 class="section-title" style="top:325px">Our Industries</h2>
  <svg class="arrow" style="left:649px;top:326px" viewBox="0 0 14 24"><path d="M2 3 L10 12 L2 21" stroke="#555" stroke-width="2.6" fill="none"/></svg>
  <div class="cards" style="top:352px">
    <div class="card"><div class="card-label">Restaurants and Cafes</div><div class="card-img" role="img" aria-label="Restaurant dining room" style="background:linear-gradient(#4a4f5a,#8a7a66)"></div><p class="card-text">Lorem Ipsum is simply dummy text of the printing and typesetting industry. Lorem Ipsum has been the industry's standard</p><span class="btn">Read More</span></div>
    <div class="card"><div class="card-label">Grocery and Convenience</div><div class="card-img" role="img" aria-label="Shopper in a grocery aisle" style="background:linear-gradient(120deg,#8a7d70,#6a8fb0)"></div><p class="card-text">Lorem Ipsum is simply dummy text of the printing and typesetting industry. Lorem Ipsum has been the industry's standard</p><span class="btn">Read More</span></div>
    <div class="card"><div class="card-label">Fruit &amp; Veg</div><div class="card-img" role="img" aria-label="Woman carrying fresh fruit and vegetables" style="background:linear-gradient(120deg,#a7ae3a,#6f8a1e)"></div><p class="card-text">Lorem Ipsum is simply dummy text of the printing and typesetting industry. Lorem Ipsum has been the industry's standard</p><span class="btn">Read More</span></div>
    <div class="card"><div class="card-label">Bars</div><div class="card-img" role="img" aria-label="Friends enjoying drinks at a bar" style="background:linear-gradient(120deg,#2b3a8a,#b0602a)"></div><p class="card-text">Lorem Ipsum is simply dummy text of the printing and typesetting industry. Lorem Ipsum has been the industry's standard</p><span class="btn">Read More</span></div>
  </div>
</section>

<section>
  <svg class="arrow" style="left:80px;top:580px" viewBox="0 0 14 24"><path d="M12 3 L4 12 L12 21" stroke="#555" stroke-width="2.6" fill="none"/></svg>
  <h2 class="section-title" style="top:584px">Videos Testimonials</h2>
  <svg class="arrow" style="left:649px;top:580px" viewBox="0 0 14 24"><path d="M2 3 L10 12 L2 21" stroke="#555" stroke-width="2.6" fill="none"/></svg>
  <div class="cards" style="top:621px">
    <div class="card"><div class="card-img" role="img" aria-label="Video testimonial from a cafe owner" style="background:linear-gradient(120deg,#7a5a4a,#b9a898)"></div><div class="card-title">Grocery Point of Sale System</div><div class="card-meta">Tuesday, 03 May 2011 17:04 Leah Morton</div><div class="quote">“</div><p class="card-text">Lorem Ipsum is simply dummy text of the printing and typesetting industry. Lorem Ipsum has been the industry's standard</p><span class="btn">Read More</span></div>
    <div class="card"><div class="card-img" role="img" aria-label="Video testimonial from a grocer" style="background:linear-gradient(120deg,#333,#6a7a5a)"></div><div class="card-title">Grocery Point of Sale System</div><div class="card-meta">Tuesday, 03 May 2011 17:04 Leah Morton</div><div class="quote">“</div><p class="card-text">Lorem Ipsum is simply dummy text of the printing and typesetting industry. Lorem Ipsum has been the industry's standard</p><span class="btn">Read More</span></div>
    <div class="card"><div class="card-img" role="img" aria-label="Video testimonial from a reseller" style="background:linear-gradient(120deg,#111,#2a3f8a)"></div><div class="card-title">Grocery Point of Sale System</div><div class="card-meta">Tuesday, 03 May 2011 17:04 Leah Morton</div><div class="quote">“</div><p class="card-text">Lorem Ipsum is simply dummy text of the printing and typesetting industry. Lorem Ipsum has been the industry's standard</p><span class="btn">Read More</span></div>
    <div class="card"><div class="card-img" role="img" aria-label="Video testimonial from a bar" style="background:linear-gradient(120deg,#3a2a20,#9a6a40)"></div><div class="card-title">Grocery Point of Sale System</div><div class="card-meta">Tuesday, 03 May 2011 17:04 Leah Morton</div><div class="quote">“</div><p class="card-text">Lorem Ipsum is simply dummy text of the printing and typesetting industry. Lorem Ipsum has been the industry's standard</p><span class="btn">Read More</span></div>
  </div>
  <svg style="position:absolute;left:0;top:0" width="742" height="1200" aria-hidden="true">
    <g fill="none" stroke="#fff" stroke-width="2"><circle cx="148" cy="661" r="15"/><circle cx="296" cy="661" r="15"/><circle cx="444" cy="661" r="15"/><circle cx="592" cy="661" r="15"/></g>
    <g fill="#fff"><path d="M143 653 L157 661 L143 669Z"/><path d="M291 653 L305 661 L291 669Z"/><path d="M439 653 L453 661 L439 669Z"/><path d="M587 653 L601 661 L587 669Z"/></g>
  </svg>
</section>

<section>
  <h2 class="section-title" style="top:878px">Our products</h2>
  <div class="products">
    <div class="product"><div class="product-frame"><div class="pic" role="img" aria-label="Touch screen point of sale terminal" style="background:linear-gradient(#4a4a4a,#1c1c1c);border-radius:6px;width:82px"></div></div><p class="product-text">Fast graphical touch screen systems built for busy counters in cafes, grocers, fruit shops and bars.</p><span class="btn">Buy Online</span></div>
    <div class="product"><div class="product-frame promo promo-sale"><div class="promo-kicker">Limited time</div><div class="promo-title">End Of Financial<br>Year Sale</div><div class="promo-note">Save on complete touch screen systems</div></div><p class="product-text">Upgrade before 30 June and claim your new point of sale system in this financial year.</p><span class="btn">Shop the Sale</span></div>
    <div class="product"><div class="product-frame promo promo-finance"><div class="promo-kicker">Pay your way</div><div class="promo-title">Finance Options</div><div class="promo-note">Flexible weekly plans for every business</div></div><p class="product-text">Spread the cost of your system with simple rental and finance plans to suit your cash flow.</p><span class="btn">Apply Now</span></div>
  </div>
</section>

<footer class="site-footer">
  <nav class="footer-nav">
    <span>Home</span><span>|</span><span>Our System</span><span>|</span><span>About Us</span><span>|</span><span>Events</span><span>|</span><span>Testimonials</span><span>|</span><span>Blog</span><span>|</span><span>Gallery</span><span>|</span><span>Contact</span>
  </nav>
  <p class="copyright">© 2014 Company Name ,All Rights Reserved</p>
</footer>
</body>
</html>
```